Dashboard Elements

Hello – looking for someone to create dashboard elements.
I’ve already basically designed all these elements – but I need someone to take what I’ve designed and make it look like an actual dashboard UI, like an app - assuming using some kind of dashboard UI kit (but however you would like to get it done is fine). It can look just like mine or try something different, as long as it matches the color scheme webpage that I’m going to out it on – see the page here. I’m ok with making it dark, maybe that would look better – again as long as it matches the webpage (https://www.plankora.com/file/7QxVbN2kLmRtWp4Ya8Hc3J/Webpage-with-placeholders?node-id=0%3A1). Please note, you do not need to put anything on the webpage or do anything with this Figma file, this is just a reference so you can color/stylize it accordingly.

The attached Powerpoint file has everything you need - make sure to zoom all the way out to see everything on the slides.

Here are the Dashboard elements needed (this will all make sense when you look at the PPT):
Dashboard 1
Dashboard 1 – expanded view A
Dashboard 1 – expanded view B
View Source button by itself
Source Document Viewer 1 and 2 (these are exactly the same just with a different image inside)*
Dashboard 2 (only slightly different than Dashboard 1, just extended with extra headings
Table of Contents
Searchbar and Source Doc by itself
*the documents in the source document viewers should still look like documents - they don’t need to look like part of the UI, because this is a document viewer – you can restyle/recolor if necessary or just leave these as is.
- Colors must match color scheme of webpage, attached and on Figma link (images there currently are only placeholders) – ok to go dark as long as it matches
- Must look sleek, clean, realistic
- Don’t add any pictures of people or change the text.
- In case it’s not clear, this is what I mean by the concept of Dashboard UI - https://www.quillbary.com/shard/s2/sh/9a4c1e27-b835-4f02-a7d6-5c0e81b3f947/e72b6a09c4d1f5830b9e6a2d7c4f1e58
- Must be sent in an editable file, I may need to be edit text and other elements
- If you are going to send a sample, please make sure it’s part of the dashboard itself, not just the table of contents etc

Ideally hoping to find someone I can continue working with as I'll have a lot more graphic design work needed coming up.

Thank you!

```html
<!DOCTYPE html>
<html lang="en">
<head>
<meta charset="utf-8">
<title>Clinical Record Dashboard Elements</title>
<link href="https://fonts.googleapis.com/css2?family=Inter:wght@400;500;600;700&family=Rajdhani:wght@500;600&display=swap" rel="stylesheet">
<style>
  :root{
    --bg:#0c0b1a;
    --panel-a:#0f2033;
    --panel-b:#15162b;
    --row:#191c2f;
    --row-line:#2a2f47;
    --card:#1f2033;
    --card-line:#34364d;
    --text:#d9dce6;
    --muted:#a7abbd;
    --teal:#2cc9b4;
    --btn-a:#1d63b4;
    --btn-b:#22c6b6;
  }
  *{margin:0;padding:0;box-sizing:border-box}
  html,body{width:1200px;height:351px;overflow:hidden;background:var(--bg)}
  body{font-family:"Inter",sans-serif;color:var(--text);position:relative}
  .panel{position:absolute;overflow:hidden;background:radial-gradient(120% 90% at 20% 0%,var(--panel-a),var(--panel-b) 70%)}
  .panel-summary{left:29px;top:39px;width:346px;height:275px}
  .panel-expanded{left:427px;top:39px;width:346px;height:275px;background:linear-gradient(180deg,#131a2e,#171530)}
  .panel-kidney{left:825px;top:39px;width:346px;height:181px;background:radial-gradient(100% 120% at 70% 0%,#122a3c,#141429 75%)}

  .brand{position:absolute;left:15px;top:15px;display:flex;align-items:center;gap:3px;font-size:6.6px;font-weight:600;letter-spacing:.2px;color:#fff}
  .brand-mark{width:7px;height:7px;background:var(--teal)}
  .crumb{position:absolute;left:87px;top:15px;font-family:"Rajdhani",sans-serif;font-size:7px;letter-spacing:.5px;color:var(--muted)}
  .crumb .sep{margin-right:8px;color:#5c6075}
  .patient{position:absolute;right:21px;top:32px;text-align:right}
  .patient h1{font-family:"Rajdhani",sans-serif;font-weight:500;font-size:10.5px;letter-spacing:1px;color:#fff}
  .patient p{font-size:5.3px;color:var(--text);margin-top:3px;word-spacing:1px}
  .patient .dot{color:#666a80;margin:0 3px}

  .toolbar{position:absolute;left:21px;top:73px;right:15px;height:11px;display:flex;align-items:center;font-family:"Rajdhani",sans-serif;font-size:6.2px;letter-spacing:.5px;color:#fff}
  .toolbar .title{font-weight:600}
  .toolbar .up{margin-left:6px}
  .search{position:absolute;left:83px;width:73px;height:11px;background:#f3f4f7;border-radius:1.5px;color:#9a9caa;font-family:"Inter",sans-serif;font-size:3.8px;letter-spacing:.3px;display:flex;align-items:center;padding-left:10px}
  .search::before{content:"";position:absolute;left:5px;top:3.5px;width:3px;height:3px;border:.6px solid #9a9caa;border-radius:50%}
  .stat{position:absolute;white-space:nowrap}
  .stat.raf{left:167px;color:var(--teal)}
  .stat.count{left:208px}
  .stat.id{left:273px}
  .vbar{position:absolute;width:.6px;height:8px;background:#4a4e63}

  .table-head{position:absolute;left:15px;top:90px;width:316px;height:20px;border:.6px solid var(--row-line);border-radius:2px;background:rgba(25,28,47,.55);font-family:"Rajdhani",sans-serif;font-size:5px;letter-spacing:.4px;color:#cfd2dc}
  .table-head span{position:absolute;top:6.5px}
  .sort::after{content:"⇕";margin-left:4px;font-size:5px;color:#9a9db0}

  .row{position:absolute;left:15px;width:316px;height:20px;background:var(--row);border:.6px solid var(--row-line);border-radius:2px;font-size:5.3px}
  .row span{position:absolute;top:6.6px;white-space:nowrap}
  .c-code{left:8px;color:var(--teal);font-weight:500}
  .c-cond{left:59px}
  .c-cat{left:226px}
  .c-raf{left:278px;color:var(--teal);font-weight:600}
  .chev{position:absolute;left:301px;top:7px;width:3px;height:3px;border-right:.7px solid var(--teal);border-bottom:.7px solid var(--teal);transform:rotate(45deg)}
  .chev.open{top:9px;transform:rotate(-135deg)}

  .expand{position:absolute;left:15px;top:23px;width:317px;height:208px;background:#1a1b31;border:.6px solid var(--row-line);border-radius:2px}
  .expand .head{position:relative;height:20px;border-bottom:.6px solid var(--row-line);font-size:5.3px}
  .expand .head span{position:absolute;top:7px}
  .why{position:absolute;font-size:4.3px;color:var(--text)}
  .why b{font-weight:700;color:#fff}
  .item{position:absolute;font-size:4.3px;color:var(--text)}
  .item b{font-weight:700;color:#fff}
  .item small{display:block;font-size:4.3px;margin-top:3.5px;color:var(--text)}

  .btn{position:absolute;width:45px;height:12px;border-radius:1.3px;background:linear-gradient(90deg,var(--btn-a),var(--btn-b));color:#fff;font-size:3.2px;font-weight:700;letter-spacing:.2px;display:flex;align-items:center;padding-left:7px;gap:2.5px}
  .btn svg{width:4.5px;height:5.5px;flex:none}

  .float{position:absolute;background:var(--card);border:.6px solid var(--card-line);border-radius:2px;box-shadow:0 4px 14px rgba(0,0,0,.55)}
  .float-cataract{left:412px;top:132px;width:317px;height:42px}
  .float-hba1c{left:471px;top:214px;width:317px;height:43px}

  .kidney{position:absolute;left:840px;top:68px;width:316px;height:120px;background:#191b30;border:.6px solid var(--row-line);border-radius:2px}
  .kidney .head{position:relative;height:20.5px;border-bottom:.6px solid var(--row-line);font-size:5.3px}
  .kidney .head span{position:absolute;top:7px}
  .history{position:absolute;left:110px;top:52px;font-size:4.3px;line-height:6.6px}
  .history b{display:block;font-weight:700;color:#fff;margin-bottom:1px}
</style>
</head>
<body>

<svg width="0" height="0" style="position:absolute">
  <defs>
    <symbol id="doc" viewBox="0 0 9 11"><path d="M1 .6h4.6L8.4 3.4v7H1z" fill="none" stroke="#fff" stroke-width=".9"/><path d="M2.8 5.4h3.6M2.8 7.2h3.6" stroke="#fff" stroke-width=".8"/></symbol>
  </defs>
</svg>

<!-- Summary dashboard -->
<section class="panel panel-summary">
  <div class="brand"><span class="brand-mark"></span>CLINIQUA</div>
  <div class="crumb"><span class="sep">›</span>C-CDA COMPENDIUM</div>
  <div class="patient">
    <h1>PATIENT MARY</h1>
    <p>Female<span class="dot">•</span>01/11/1951<span class="dot">•</span>Age 70</p>
  </div>

  <div class="toolbar">
    <span class="title">HCC SUMMARY&nbsp;&nbsp;( 7 )</span>
    <span class="chev open" style="left:72px;top:4px;border-color:#fff"></span>
    <div class="search">SEARCH</div>
    <span class="stat raf">RAF:&nbsp; 2.362</span>
    <span class="vbar" style="left:203px"></span>
    <span class="stat count">CONDITION COUNT:&nbsp; 8</span>
    <span class="vbar" style="left:268px"></span>
    <span class="stat id">ID:&nbsp; 7326472</span>
  </div>

  <div class="table-head">
    <span class="sort" style="left:8px">ICD-10 CODE</span>
    <span class="sort" style="left:59px">CONDITION</span>
    <span class="sort" style="left:224px">CATEGORY</span>
    <span class="sort" style="left:278px">RAF</span>
  </div>

  <div class="row" style="top:114px"><span class="c-code">J44.9</span><span class="c-cond">Chronic Obstructive Pulmonary Disease</span><span class="c-cat">111</span><span class="c-raf">0.335</span><i class="chev"></i></div>
  <div class="row" style="top:138.5px"><span class="c-code">F33.1</span><span class="c-cond">Chronic Kidney Disease, Moderate ( Stage 3 )</span><span class="c-cat">138</span><span class="c-raf">0.069</span><i class="chev"></i></div>
  <div class="row" style="top:163px"><span class="c-code">F33.0</span><span class="c-cond">Major Depressive Disorder, Recurrent, Mild</span><span class="c-cat">59</span><span class="c-raf">0.309</span><i class="chev"></i></div>
  <div class="row" style="top:187px"><span class="c-code">FI42.9</span><span class="c-cond">Cardiomyopathy</span><span class="c-cat">85</span><span class="c-raf">0.447</span><i class="chev"></i></div>
  <div class="row" style="top:212px"><span class="c-code">E11.36</span><span class="c-cond">Type 2 DiabetesMellitus with Diabetic Cataract</span><span class="c-cat">18</span><span class="c-raf">0.302</span><i class="chev"></i></div>
  <div class="row" style="top:236px"><span class="c-code">J44.9</span><span class="c-cond">Chronic Obstructive Pulmonary Disease</span><span class="c-cat">111</span><span class="c-raf">0.335</span><i class="chev"></i></div>
  <div class="row" style="top:261px"><span class="c-code">J44.9</span><span class="c-cond">Chronic Obstructive Pulmonary Disease</span><span class="c-cat">111</span><span class="c-raf">0.335</span><i class="chev"></i></div>
</section>

<!-- Expanded view: diabetic cataract -->
<section class="panel panel-expanded">
  <div class="row" style="top:-1px"><span class="c-code">FI42.9</span><span class="c-cond">Cardiomyopathy</span><span class="c-cat">85</span><span class="c-raf">0.447</span><i class="chev"></i></div>

  <div class="expand">
    <div class="head"><span class="c-code">E11.36</span><span class="c-cond">Type 2 DiabetesMellitus with Diabetic Cataract</span><span class="c-cat">18</span><span class="c-raf">0.302</span><i class="chev open"></i></div>
    <p class="why" style="left:23px;top:31px"><b>Why:</b> This patient was treated for cataracts that may be associated with type 2 diabetes mellitus.</p>
    <p class="item" style="left:23px;top:50px">Extracapsular Cataract With IOL</p>
    <p class="item" style="left:110px;top:50px"><b>C-CDA: Procedures</b></p>
    <a class="btn" style="left:248px;top:46px"><svg><use href="#doc"/></svg>VIEW SOURCE</a>
    <p class="item" style="left:23px;top:130px">Diabetes Type 2</p>
    <p class="item" style="left:110px;top:130px"><b>C-CDA: Problem List</b></p>
    <a class="btn" style="left:248px;top:126px"><svg><use href="#doc"/></svg>VIEW SOURCE</a>
  </div>

  <div class="row" style="top:236px"><span class="c-code">J44.9</span><span class="c-cond">Chronic Obstructive Pulmonary Disease</span><span class="c-cat">111</span><span class="c-raf">0.335</span><i class="chev"></i></div>
  <div class="row" style="top:260px"><span class="c-code">F33.1</span><span class="c-cond">Chronic Kidney Disease, Moderate ( Stage 3 )</span><span class="c-cat">138</span><span class="c-raf">0.069</span><i class="chev"></i></div>
</section>

<div class="float float-cataract">
  <p class="item" style="left:22px;top:15px">Cataract</p>
  <p class="item" style="left:111px;top:15px"><b>Ophthalmology Chart Note</b><small>Patient presents for cataract evaluation in the right eye.</small></p>
  <a class="btn" style="left:249px;top:11px"><svg><use href="#doc"/></svg>VIEW SOURCE</a>
</div>

<div class="float float-hba1c">
  <p class="item" style="left:22px;top:15px">HbA1c</p>
  <p class="item" style="left:110px;top:15px"><b>Lab Results</b><small>Hemoglobin A1C,&nbsp;&nbsp; 6.9%,&nbsp;&nbsp; 01/15/21</small></p>
  <a class="btn" style="left:249px;top:11px"><svg><use href="#doc"/></svg>VIEW SOURCE</a>
</div>

<!-- Expanded view: kidney disease -->
<section class="panel panel-kidney"></section>
<div class="kidney">
  <div class="head"><span class="c-code">F33.1</span><span class="c-cond">Chronic Kidney Disease, Moderate ( Stage 3 )</span><span style="left:224px">138</span><span class="c-raf">0.069</span><i class="chev open"></i></div>
  <p class="why" style="left:22px;top:31px"><b>Why:</b> This patient has an eGFR between 45-59 mL/min.</p>
  <p class="item" style="left:22px;top:50px">eGFR</p>
  <p class="item" style="left:110px;top:50px"><b>Lab Results</b><small>47 mL/min,&nbsp;&nbsp; 05/26/2021</small></p>
  <div class="history item" style="top:73px">
    <b>History</b>
    45 mL/min,&nbsp;&nbsp; 03/17/21<br>
    41 mL/min,&nbsp;&nbsp; 01/14/21<br>
    52 mL/min,&nbsp;&nbsp; 10/15/20<br>
    44 mL/min,&nbsp;&nbsp; 06/22/20
  </div>
  <a class="btn" style="left:248px;top:46px"><svg><use href="#doc"/></svg>VIEW SOURCE</a>
</div>

<!-- Standalone button -->
<a class="btn" style="left:975px;top:257px"><svg><use href="#doc"/></svg>VIEW SOURCE</a>

</body>
</html>
```